Tamarack Hearth Partners Business Card

Looking for a new business card layout. We are a real estate firm w/ a logo, old design attached. Must keep the same elements on there, just need a fresh look and possible some foil accents. Looking for a simpler design w/ more modern style.

Target Market(s)

Real Estate clients

Industry/Entity Type

Real Estate Agent

Contact Information for Business Card

see attached

Font styles to use
Sans Serif

Requirements
Must have
• all elements on current biz card
Nice to have
• modern look, simpler than we have!
Should not have
• no serif fonts

```html
<!DOCTYPE html>
<html lang="en">
<head>
<meta charset="utf-8">
<title>Tamarack Hearth Partners – Business Card</title>
<link href="https://fonts.googleapis.com/css2?family=Poppins:wght@400;500;600;700&display=swap" rel="stylesheet">
<style>
  :root {
    --canvas: #2a2a2c;
    --card-black: #0d0d0e;
    --swoosh-dark: #1b1b1d;
    --swoosh-mid: #262628;
    --accent-red: #e2262b;
    --logo-grey: #c9c9cb;
    --back-logo: #8d8d90;
    --text-white: #ffffff;
    --text-muted: #9a9a9d;
    --photo-light: #e9e6e2;
    --photo-hair: #d8c39a;
    --photo-teal: #4fc7c9;
  }
  * { box-sizing: border-box; margin: 0; padding: 0; }
  html, body { width: 1200px; height: 880px; overflow: hidden; }
  body {
    background: var(--canvas);
    font-family: "Poppins", sans-serif;
    position: relative;
  }
  .card {
    position: absolute;
    left: 300px;
    width: 600px;
    height: 343px;
    border-radius: 16px;
    overflow: hidden;
    background: var(--card-black);
    box-shadow: 0 14px 30px rgba(0,0,0,.45);
  }
  .card--back { top: 70px; }
  .card--front { top: 467px; }

  /* Back */
  .back-logo {
    position: absolute;
    left: 150px;
    top: 110px;
    color: var(--back-logo);
    font-weight: 600;
    line-height: 1;
  }
  .back-logo .logo-top { font-size: 22px; letter-spacing: 4px; display: block; }
  .back-logo .logo-main { font-size: 50px; letter-spacing: 1px; display: block; margin-top: 4px; }
  .back-url {
    position: absolute;
    left: 36px;
    bottom: 30px;
    color: var(--text-muted);
    font-size: 12px;
    letter-spacing: 7px;
    text-transform: uppercase;
  }

  /* Front */
  .front-art, .front-photo { position: absolute; inset: 0; width: 600px; height: 343px; }
  .front-logo {
    position: absolute;
    left: 34px;
    top: 58px;
    color: var(--logo-grey);
    font-weight: 600;
    line-height: 1;
  }
  .front-logo .logo-top { font-size: 15px; letter-spacing: 3px; display: block; }
  .front-logo .logo-main { font-size: 34px; display: block; margin-top: 3px; }
  .agent { position: absolute; left: 36px; top: 152px; }
  .agent-name { color: var(--text-white); font-size: 22px; font-weight: 700; line-height: 1.1; }
  .agent-title { color: var(--text-muted); font-size: 11px; }
  .contact-list {
    position: absolute;
    left: 36px;
    top: 212px;
    list-style: none;
    color: var(--text-white);
    font-size: 12.5px;
  }
  .contact-list li { display: flex; align-items: center; gap: 9px; height: 21px; }
  .contact-list .label { color: var(--text-muted); }
  .contact-list svg { width: 15px; height: 15px; flex: none; }
  .address li:last-child { padding-left: 24px; }
</style>
</head>
<body>

<section class="card card--back" aria-label="Card back">
  <div class="back-logo">
    <span class="logo-top">TAMARACK HEARTH</span>
    <span class="logo-main">PARTNERS</span>
  </div>
  <p class="back-url">www.tamarackhearth-homes.com</p>
</section>

<section class="card card--front" aria-label="Card front">
  <svg class="front-art" viewBox="0 0 600 343" aria-hidden="true">
    <path d="M0 343 L0 250 C120 200 200 140 250 0 L330 0 C300 160 220 290 150 343 Z" fill="var(--swoosh-dark)"/>
    <path d="M150 343 C220 290 300 160 330 0 L380 0 C370 170 330 280 290 343 Z" fill="var(--swoosh-mid)"/>
    <path d="M290 343 C330 280 370 170 380 0 L410 0 C420 140 400 270 400 343 Z" fill="var(--swoosh-dark)"/>
    <path d="M300 0 C390 30 410 200 450 343" fill="none" stroke="var(--accent-red)" stroke-width="7"/>
  </svg>
  <svg class="front-photo" viewBox="0 0 600 343" role="img" aria-label="Portrait photo of the broker">
    <defs>
      <linearGradient id="photoTone" x1="0" y1="0" x2="0.4" y2="1">
        <stop offset="0" stop-color="var(--photo-light)"/>
        <stop offset="0.45" stop-color="var(--photo-hair)"/>
        <stop offset="1" stop-color="var(--photo-teal)"/>
      </linearGradient>
    </defs>
    <path d="M318 0 C410 40 420 200 466 343 L600 343 L600 0 Z" fill="url(#photoTone)"/>
  </svg>

  <div class="front-logo">
    <span class="logo-top">TAMARACK HEARTH</span>
    <span class="logo-main">PARTNERS</span>
  </div>

  <div class="agent">
    <p class="agent-name">Dana Reyes</p>
    <p class="agent-title">Principal Broker</p>
  </div>

  <ul class="contact-list address">
    <li>
      <svg viewBox="0 0 16 16"><circle cx="8" cy="8" r="7" fill="none" stroke="var(--accent-red)" stroke-width="1.3"/><path d="M5.5 4.5 L7 6 L6 7 C6.6 8.4 7.6 9.4 9 10 L10 9 L11.5 10.5 L10.5 11.5 C7.5 11 5 8.5 4.5 5.5 Z" fill="var(--accent-red)"/></svg>
      <span><span class="label">Office : </span>555.010.7222</span>
    </li>
    <li>
      <svg viewBox="0 0 16 16"><circle cx="8" cy="8" r="7" fill="none" stroke="var(--accent-red)" stroke-width="1.3"/><rect x="5.7" y="3.8" width="4.6" height="8.4" rx="0.8" fill="none" stroke="var(--accent-red)" stroke-width="1.1"/></svg>
      <span><span class="label">Cell : </span>555.010.4208</span>
    </li>
    <li>
      <svg viewBox="0 0 16 16"><circle cx="8" cy="8" r="7" fill="none" stroke="var(--accent-red)" stroke-width="1.3"/><rect x="4.3" y="5.3" width="7.4" height="5.4" fill="none" stroke="var(--accent-red)" stroke-width="1.1"/><path d="M4.3 5.3 L8 8.4 L11.7 5.3" fill="none" stroke="var(--accent-red)" stroke-width="1.1"/></svg>
      <span>dana@tamarackhearth.com</span>
    </li>
    <li>
      <svg viewBox="0 0 16 16"><circle cx="8" cy="8" r="7" fill="none" stroke="var(--accent-red)" stroke-width="1.3"/><circle cx="8" cy="8" r="3.8" fill="none" stroke="var(--accent-red)" stroke-width="1"/><path d="M4.2 8 H11.8 M8 4.2 C6.4 6 6.4 10 8 11.8 M8 4.2 C9.6 6 9.6 10 8 11.8" fill="none" stroke="var(--accent-red)" stroke-width="0.9"/></svg>
      <span>TamarackHearth-Homes.com</span>
    </li>
    <li>
      <svg viewBox="0 0 16 16"><circle cx="8" cy="8" r="7" fill="none" stroke="var(--accent-red)" stroke-width="1.3"/><path d="M8 12 C6 9.5 5.2 8.3 5.2 6.9 A2.8 2.8 0 0 1 10.8 6.9 C10.8 8.3 10 9.5 8 12 Z" fill="var(--accent-red)"/><circle cx="8" cy="6.9" r="1" fill="var(--card-black)"/></svg>
      <span>412 Juniper Ave</span>
    </li>
    <li><span>Ridgefield, OR 97000</span></li>
  </ul>
</section>

</body>
</html>
```